Verpackungsdesign für Nahrungsergänzungsmittel
Zielgruppe
Wir sind eine Firma für Nahrungsergänzungsmittel und suchen für unser neues Produkt ein Ansprechendes Etikett für die Dose. Das Produkt: GLANZ KRAFT FORM
Aufgabenstellung
Deckel: weiß, geriffelt
Etikettengröße: 145 x 50 mm
Folgender Inhalt muss auf die Dose: Siehe Screenshot 0012
Außerdem soll unser Logo drauf: Siehe Bild kelmorastil.734.png
Bitte an folgenden Beispielen orientieren:
https://www.warenhof-beispiel.de/Biltaro-Vital-Kapseln-Hochdosiert/dp/Q00000000X

```html
<!DOCTYPE html>
<html lang="de">
<head>
<meta charset="utf-8">
<title>Etikett GLANZ KRAFT FORM</title>
<link href="https://fonts.googleapis.com/css2?family=Fira+Sans:wght@300;400;500;800&family=Fira+Sans+Condensed:wght@400;600&display=swap" rel="stylesheet">
<style>
  :root {
    --green: #7cae45;
    --ink: #1b1b1b;
    --grey: #7a7a7a;
    --rule: #c9c9c9;
    --paper: #ffffff;
    --backdrop: #f2f2f2;
  }
  * { box-sizing: border-box; margin: 0; padding: 0; }
  html, body { width: 1200px; height: 566px; overflow: hidden; background: var(--backdrop); }
  .label {
    position: absolute; left: 40px; top: 90px; width: 1120px; height: 387px;
    background: var(--paper); border: 1px solid #e2e2e2;
    font-family: "Fira Sans", sans-serif; color: var(--ink);
  }
  /* Nutrition table */
  .nutrition {
    position: absolute; left: 39px; top: 21px; width: 256px;
    border-collapse: collapse; font-family: "Fira Sans Condensed", sans-serif;
    font-size: 10px; color: var(--grey);
  }
  .nutrition th {
    background: var(--green); color: #fff; font-weight: 600; font-size: 10px;
    line-height: 1; height: 40px; padding: 3px 4px; text-align: left; vertical-align: top;
    border-right: 1px solid #fff;
  }
  .nutrition th.num { text-align: right; }
  .nutrition td {
    height: 27px; padding: 2px 4px; border: 1px solid var(--rule); line-height: 1.1;
  }
  .nutrition td.num { text-align: right; }
  .nutrition tr.tall td { height: 40px; }
  .nutrition .foot td { font-size: 5px; height: 26px; vertical-align: top; border: 1px solid var(--rule); }
  /* Brand block */
  .brand {
    position: absolute; left: 420px; width: 290px; top: 0; text-align: center;
  }
  .brand-mark {
    width: 56px; height: 56px; border-radius: 50%; background: var(--green);
    margin: 30px auto 0;
  }
  .brand-name { margin-top: 14px; font-size: 22px; font-weight: 400; letter-spacing: 0.5px; color: var(--ink); }
  .product-name {
    margin-top: 10px; font-size: 42px; font-weight: 800; line-height: 45px; letter-spacing: 0.5px;
  }
  .divider { width: 172px; height: 2px; background: var(--ink); margin: 8px auto 0; }
  .subtitle { margin-top: 8px; font-size: 21px; font-weight: 500; letter-spacing: 1.5px; }
  .category { margin-top: 10px; font-size: 18px; font-weight: 300; letter-spacing: 0.5px; }
  .origin-seal {
    position: absolute; left: 657px; top: 208px; width: 76px; height: 76px;
    border: 2px solid #9a9a9a; border-radius: 50%;
  }
  /* Green band */
  .count-band {
    position: absolute; left: 2px; right: 0; top: 329px; height: 32px; background: var(--green);
    color: #fff; text-align: center; font-size: 21px; font-weight: 400; letter-spacing: 3px; line-height: 32px;
    padding-left: 0; width: calc(100% - 2px);
  }
  /* Info column */
  .info {
    position: absolute; left: 813px; top: 20px; width: 230px;
    font-size: 11px; line-height: 17px; color: var(--grey); font-weight: 300;
  }
  .info p + p { margin-top: 17px; }
  .info strong { font-weight: 500; color: #555; }
</style>
</head>
<body>
<main class="label">
  <table class="nutrition">
    <thead>
      <tr><th>Nähr- und<br>Inhaltsstoffe</th><th class="num">pro Tagesdosis<br>(2 Kapseln)</th><th class="num">% NRV*</th></tr>
    </thead>
    <tbody>
      <tr><td>Pantothensäure</td><td class="num">6 mg</td><td class="num">100%</td></tr>
      <tr><td>Vitamin B6</td><td class="num">1,4 mg</td><td class="num">100%</td></tr>
      <tr><td>Biotin</td><td class="num">51 µg</td><td class="num">100%</td></tr>
      <tr><td>Kupfer</td><td class="num">1 mg</td><td class="num">100%</td></tr>
      <tr><td>Zink</td><td class="num">10 mg</td><td class="num">100%</td></tr>
      <tr class="tall"><td>Polyporus umbellatus<br>davon Polysaccharide</td><td class="num">100 mg<br>30 mg</td><td class="num">**</td></tr>
      <tr class="tall"><td>Bambussprossen<br>—davon Silizium</td><td class="num">43,5 mg<br>32,6 mg</td><td class="num">**</td></tr>
      <tr class="foot"><td colspan="3">* Prozent Nährstoffbezugswerte (NRV) laut Verordnung (EU) Nr. 1169/2011<br>** Keine Nährstoffbezugswerte (NRV) vorhanden</td></tr>
    </tbody>
  </table>

  <section class="brand">
    <div class="brand-mark" aria-hidden="true"></div>
    <p class="brand-name">KELMORASTIL</p>
    <h1 class="product-name">GLANZ KRAFT<br>FORM</h1>
    <div class="divider"></div>
    <p class="subtitle">BIOTIN + ZINK</p>
    <p class="category">Nahrungsergänzungsmittel</p>
  </section>
  <div class="origin-seal" aria-hidden="true"></div>

  <div class="count-band">60 KAPSELN</div>

  <section class="info">
    <p><strong>Zutaten:</strong> Perlhirse-Extrakt 4:1, Trennmittel: Magnesiumsalze der Speise-fettsäuren, Überzugsmittel: Hydroxypropylmethyl-cellulose, Eichhase-Extrakt (Polyporus umbellatus; 30 % Polysaccharide), Zink-gluconat, Bambussprossen-Extrakt 5:1 (75 % Silizium), Kupfergluconat, Calcium-D-pantotheriat, Pyridoxinhydro-chlorid, D-Biotin.</p>
    <p><strong>Verzehrempfehlung:</strong> 2 Kapseln täglich mit reichlich Flüssigkeit einnehmen.</p>
    <p>Hergestellt für<br>Talmark Versand GmbH<br>Lindenweg 14<br>79000 Musterstadt</p>
  </section>
</main>
</body>
</html>
```